Corporate Template

Looking for a set of corporate slides to be made which contain multiple different slides and orientations. Looking for at least 8 to 10 different master pages plus a Coversheet and closeout page. Incorporating a color palate similar to our logo coloring is preferred.
I have attached a logo.
I like the clever pixel yard designs best so far. They seem to fit what I'm looking for in terms of visual appearance.
Reason: I'm trying to allow time for a couple new designers to incorporate some changes I requested to their existing designs.

```html
<!DOCTYPE html>
<html lang="en">
<head>
<meta charset="utf-8">
<title>Our Management Skill</title>
<link rel="stylesheet" href="https://fonts.googleapis.com/css2?family=Ubuntu:wght@400;500;700&display=swap">
<style>
  :root {
    --blue-deep: #2c66a3;
    --blue-mid: #3573b0;
    --blue-sky: #5ea5e6;
    --blue-pale: #99ccfb;
    --blue-title: #9dd0ff;
    --grey-light: #c0c0c0;
    --grey-mid: #808080;
    --grey-dark: #595959;
    --ink: #161616;
    --white: #ffffff;
  }
  html, body {
    margin: 0;
    padding: 0;
    overflow: hidden;
    background: var(--white);
  }
  .slide {
    position: relative;
    width: 1200px;
    height: 900px;
    overflow: hidden;
    background: var(--white);
    font-family: "Ubuntu", "Trebuchet MS", sans-serif;
  }
  .slide-header {
    position: absolute;
    left: 0; top: 0;
    width: 1200px;
    height: 93px;
    background: linear-gradient(90deg, var(--blue-deep), #2f74bb);
    border-bottom: 6px solid var(--blue-pale);
  }
  .slide-title {
    position: absolute;
    left: 22px;
    top: 22px;
    margin: 0;
    font-size: 36px;
    font-weight: 700;
    color: var(--blue-title);
    letter-spacing: 0.2px;
  }
  .header-mark {
    position: absolute;
    right: 16px;
    top: 11px;
    width: 66px;
    height: 66px;
    border-radius: 50%;
    background: var(--blue-mid);
    border: 4px solid var(--white);
    box-sizing: border-box;
  }
  .chart {
    position: absolute;
    left: 0; top: 0;
  }
  .slice { stroke: var(--white); stroke-width: 3; }
  .label {
    font-family: "Ubuntu", "Trebuchet MS", sans-serif;
    font-size: 21px;
    font-weight: 500;
    text-anchor: middle;
  }
  .label-dark { fill: var(--ink); }
  .label-light { fill: var(--white); }
  .footer { position: absolute; left: 0; top: 0; }
  .brand {
    position: absolute;
    left: 32px;
    top: 806px;
    margin: 0;
    font-size: 30px;
    font-weight: 500;
    color: var(--white);
  }
  .copyright {
    position: absolute;
    left: 787px;
    top: 865px;
    font-size: 19px;
    color: var(--blue-title);
  }
  .page-number {
    position: absolute;
    left: 1140px;
    top: 828px;
    width: 48px;
    height: 48px;
    border-radius: 50%;
    border: 3px solid var(--white);
    box-sizing: border-box;
    background: var(--blue-deep);
    color: var(--white);
    font-size: 17px;
    font-weight: 700;
    display: flex;
    align-items: center;
    justify-content: center;
  }
</style>
</head>
<body>
<main class="slide">
  <header class="slide-header">
    <h1 class="slide-title">Our Mangement SKill</h1>
    <div class="header-mark" aria-hidden="true"></div>
  </header>

  <svg class="chart" width="1200" height="900" viewBox="0 0 1200 900" role="img" aria-label="Pie chart with six segments">
    <path class="slice" fill="var(--grey-light)" d="M532 490 L532 194 A296 296 0 0 1 706 250.5 Z"/>
    <path class="slice" fill="var(--blue-pale)" d="M532 490 L706 250.5 A296 296 0 0 1 812.7 583.9 Z"/>
    <path class="slice" fill="var(--blue-sky)" d="M532 490 L812.7 583.9 A296 296 0 0 1 640.5 765.4 Z"/>
    <path class="slice" fill="var(--blue-mid)" d="M532 490 L640.5 765.4 A296 296 0 0 1 252.1 586.4 Z"/>
    <path class="slice" fill="var(--grey-dark)" d="M532 490 L252.1 586.4 A296 296 0 0 1 366.5 244.6 Z"/>
    <path class="slice" fill="var(--grey-mid)" d="M532 490 L366.5 244.6 A296 296 0 0 1 532 194 Z"/>

    <circle cx="532" cy="490" r="45" fill="var(--white)"/>
    <circle cx="532" cy="490" r="37" fill="var(--blue-mid)"/>

    <text class="label label-dark" x="591" y="280"><tspan x="591">Lorem</tspan><tspan x="591" dy="31">ipsum</tspan><tspan x="591" dy="31">dolor</tspan></text>
    <text class="label label-light" x="477" y="280"><tspan x="477">Lorem</tspan><tspan x="477" dy="31">ipsum</tspan><tspan x="477" dy="31">dolor</tspan></text>
    <text class="label label-dark" x="711" y="448"><tspan x="711">Lorem ipsum</tspan><tspan x="711" dy="31">dolor</tspan></text>
    <text class="label label-dark" x="673" y="610"><tspan x="673">Lorem ipsum</tspan><tspan x="673" dy="31">dolor</tspan></text>
    <text class="label label-dark" x="452" y="629"><tspan x="452">Lorem ipsum dolor</tspan><tspan x="452" dy="30">Lorem ipsum dolor</tspan></text>
    <text class="label label-light" x="367" y="439"><tspan x="367">Lorem ipsum dolor</tspan><tspan x="367" dy="30">Lorem ipsum dolor</tspan></text>
  </svg>

  <svg class="footer" width="1200" height="900" viewBox="0 0 1200 900" aria-hidden="true">
    <defs>
      <linearGradient id="footer-fill" x1="0" y1="0" x2="1" y2="0">
        <stop offset="0" stop-color="#2b64a0"/>
        <stop offset="1" stop-color="#2f72b6"/>
      </linearGradient>
      <radialGradient id="pattern-glow" cx="0.75" cy="0.6" r="0.6">
        <stop offset="0" stop-color="#5a96d2" stop-opacity="0.55"/>
        <stop offset="1" stop-color="#5a96d2" stop-opacity="0"/>
      </radialGradient>
    </defs>
    <path d="M0 732 C260 790 470 840 700 838 C900 836 1060 770 1200 716 L1200 900 L0 900 Z" fill="var(--blue-pale)"/>
    <path d="M0 742 C260 800 470 848 700 846 C900 844 1060 780 1200 728 L1200 900 L0 900 Z" fill="url(#footer-fill)"/>
  </svg>
  <svg class="footer" width="1200" height="900" viewBox="0 0 1200 900" role="img" aria-label="Faint dot pattern with a heartbeat line">
    <rect x="860" y="740" width="340" height="160" fill="url(#pattern-glow)"/>
  </svg>

  <p class="brand">Northfield Neuro Labs</p>
  <span class="copyright">Copyright text here</span>
  <span class="page-number">01</span>
</main>
</body>
</html>
```